Vexora and pinlark ads

Create four total ads, two for vexora and two for pinlark for classfinchly.com.

The pinlark ads will be a single image, and I will handle the text. Image should be consistent with this: https://notes.plankweave.net/image-ad-specs. Image ratio is 1200x628 with an Image ratio of 1.91:1.

Target Market(s)

Parents who have young kids and are thinking about moving to a better school district.

Industry/Entity Type

Real Estate

Font styles to use
Sans Serif

Requirements
Must have
• Classfinchly logo.

```html
<!DOCTYPE html>
<html lang="en">
<head>
<meta charset="utf-8">
<title>Classfinchly – Top 30 Chicagoland Schools</title>
<link rel="stylesheet" href="https://fonts.googleapis.com/css2?family=Days+One&family=Open+Sans:wght@400;600&display=swap">
<style>
  :root {
    --board-top: #3f9a90;
    --board-mid: #2b7d74;
    --board-deep: #1d5e58;
    --headline-ink: #1d3a28;
    --headline-halo: #ffffff;
    --band-bg: #ffffff;
    --band-ink: #2a2a2a;
  }
  * { margin: 0; padding: 0; box-sizing: border-box; }
  html, body {
    width: 1200px;
    height: 2400px;
    overflow: hidden;
    background: var(--band-bg);
  }
  .ad {
    position: relative;
    width: 1200px;
    height: 2400px;
    overflow: hidden;
  }
  .hero-photo {
    position: absolute;
    left: 0; top: 0;
    width: 1200px;
    height: 2080px;
    background:
      radial-gradient(ellipse 520px 760px at 560px 1050px, rgba(20,40,80,0.55), rgba(20,40,80,0) 70%),
      linear-gradient(180deg, var(--board-top) 0%, var(--board-mid) 55%, var(--board-deep) 100%);
  }
  .headline {
    position: absolute;
    left: 0; top: 0;
    width: 1200px;
    height: 2080px;
    font-family: "Days One", sans-serif;
    font-weight: 400;
    color: var(--headline-ink);
    text-shadow:
      0 0 6px var(--headline-halo),
      0 0 10px var(--headline-halo),
      0 0 16px var(--headline-halo),
      0 0 22px var(--headline-halo);
  }
  .headline span {
    position: absolute;
    left: 0;
    width: 1200px;
    text-align: center;
    line-height: 1;
    white-space: nowrap;
  }
  .line-intro    { font-size: 110px; top: 300px; }
  .line-number   { font-size: 172px; top: 497px; }
  .line-region   { font-size: 158px; top: 753px; }
  .line-schools  { font-size: 104px; top: 1031px; }
  .line-homes    { font-size: 115px; top: 1269px; }
  .line-match    { font-size: 109px; top: 1512px; }
  .line-needs    { font-size: 107px; top: 1761px; }
  .cta-band {
    position: absolute;
    left: 0; top: 2080px;
    width: 1200px;
    height: 320px;
    background: var(--band-bg);
    text-align: center;
  }
  .cta-lead {
    margin-top: 88px;
    font-family: "Open Sans", sans-serif;
    font-weight: 400;
    font-size: 42px;
    line-height: 1;
    color: var(--band-ink);
  }
  .brand-name {
    display: block;
    margin-top: 30px;
    font-family: "Open Sans", sans-serif;
    font-weight: 600;
    font-size: 104px;
    line-height: 1.1;
    color: var(--band-ink);
  }
</style>
</head>
<body>
  <main class="ad">
    <div class="hero-photo" role="img" aria-label="Person reading a blue book at a desk in front of a green chalkboard covered in math notes"></div>
    <h1 class="headline">
      <span class="line-intro">Find the</span>
      <span class="line-number">Top 30</span>
      <span class="line-region">Chicagoland</span>
      <span class="line-schools">Schools with</span>
      <span class="line-homes">Homes for Sale</span>
      <span class="line-match">that Match Your</span>
      <span class="line-needs">Requirements</span>
    </h1>
    <footer class="cta-band">
      <p class="cta-lead">To Learn More Visit</p>
      <span class="brand-name">Classfinchly</span>
    </footer>
  </main>
</body>
</html>
```